Venlox - Property Management Company Listings - PSD / uncoded only

Our site simply connects property owners with property managers. I’m asking you to create 2 pages, 1 homepage and 1 page that lists of property management companies. Build with Responsive Design in mind. PSD/uncoded files only. Help us create a great site!
Example competitor sites:
http://www.everyestatehelp.example/
http://www.tendyourlots.example/
Inspired by these sites:
http://www.quorvik.example/
http://www.bespokely.example/
http://www.coinwire.example/
https://www.tripboard.example/
I've attached the logo as well as 2 picture files that you can consider using.
• Venlox Logo Colors: Yellow: HTML code: #FBC30A, RGB code: R: 251 G: 195 B: 10 Grey: HTML code: #4E4C4D, RGB code: R: 78 G: 76 B: 77
• The picture files are optional.
o One picture is of houses and neighborhood.
o The other is of a professional woman on the phone. Please do not use the professional woman as a large primary image. You can use the professional woman photo as a smaller photo and not the main photo.
• Please bring your own pictures and graphics too. Don't feel like you need to use mine.
Thank you!

```html
<!DOCTYPE html>
<html lang="en">
<head>
<meta charset="utf-8">
<title>Venlox – Find your Local Property Manager</title>
<link rel="stylesheet" href="https://fonts.googleapis.com/css2?family=Mulish:wght@400;600;700;800&display=swap">
<style>
  :root {
    --brand-yellow: #fbc30a;
    --brand-grey: #4e4c4d;
    --footer-bg: #4a4a4a;
    --text-dark: #3b3b3b;
    --text-mid: #666666;
    --text-light: #ffffff;
    --field-bg: #ffffff;
    --overlay: rgba(40, 40, 40, 0.72);
  }
  * { box-sizing: border-box; margin: 0; padding: 0; }
  html, body { width: 746px; height: 1200px; overflow: hidden; }
  body {
    position: relative;
    font-family: "Mulish", sans-serif;
    color: var(--text-dark);
    background: #ffffff;
  }
  .abs { position: absolute; }

  /* Header */
  .site-header { left: 0; top: 0; width: 746px; height: 62px; background: #fff; }
  .brand { left: 80px; top: 14px; font-size: 28px; font-weight: 800; color: var(--brand-grey); letter-spacing: -0.5px; line-height: 1; }
  .main-nav { left: 337px; top: 27px; display: flex; gap: 19px; font-size: 10.5px; color: var(--brand-grey); }
  .social-top { left: 615px; top: 25px; display: flex; gap: 6px; }
  .social-top span { width: 13px; height: 13px; border-radius: 50%; background: #b8b8b8; display: block; }

  /* Hero */
  .hero {
    left: 0; top: 62px; width: 746px; height: 338px;
    background: linear-gradient(180deg, #6f8a4a 0%, #8a8f7c 25%, #8a7f78 55%, #9a938c 80%, #7d7a72 100%);
  }
  .search-panel { left: 176px; top: 174px; width: 379px; height: 113px; background: var(--overlay); }
  .search-title { left: 0; top: 14px; width: 379px; text-align: center; color: var(--text-light); font-size: 18px; font-weight: 400; }
  .field { top: 44px; height: 22px; background: var(--field-bg); border: 1px solid #d6d6d6; font-size: 7.5px; color: #888; padding: 7px 8px 0; }
  .field-type { left: 20px; width: 175px; }
  .field-type svg { position: absolute; right: 7px; top: 8px; }
  .field-zip { left: 201px; width: 80px; }
  .search-btn { left: 285px; top: 44px; width: 72px; height: 22px; background: var(--brand-yellow); color: var(--brand-grey); font-size: 11px; text-align: center; line-height: 22px; }
  .search-note { left: 40px; top: 73px; width: 299px; text-align: center; color: #e6e6e6; font-size: 8px; line-height: 12px; }
  .slider-dots { left: 362px; top: 383px; display: flex; gap: 3px; }
  .slider-dots span { width: 8px; height: 8px; border-radius: 50%; background: #fff; display: block; }

  /* Steps */
  .steps-heading { left: 0; top: 424px; width: 746px; text-align: center; font-size: 16px; color: var(--text-dark); }
  .step { top: 466px; width: 140px; text-align: center; }
  .step-icon { width: 68px; height: 68px; border-radius: 50%; background: var(--brand-yellow); margin: 0 auto; display: flex; align-items: center; justify-content: center; }
  .step-label { margin-top: 8px; font-size: 9.8px; line-height: 15px; color: var(--text-mid); }

  /* Experience band */
  .experience {
    left: 0; top: 601px; width: 746px; height: 276px;
    background: linear-gradient(90deg, #e9ebea 0%, #d9dbda 35%, #c9c5c0 55%, #5a5658 75%, #d5d3cf 100%);
  }
  .notch { left: 365px; top: 601px; }
  .experience-title { left: 78px; top: 671px; font-size: 18.5px; line-height: 24px; color: var(--text-dark); }
  .benefits { left: 78px; top: 725px; list-style: none; font-size: 9px; color: var(--text-dark); }
  .benefits li { display: flex; align-items: center; gap: 5px; height: 18px; }
  .experience-copy { left: 81px; top: 767px; width: 265px; font-size: 7.3px; line-height: 13px; color: #777; }

  /* Manager call-out */
  .manager-cta { left: 0; top: 877px; width: 746px; height: 214px; background: var(--brand-yellow); }
  .cta-icon { left: 351px; top: 906px; }
  .cta-title { left: 0; top: 959px; width: 746px; text-align: center; color: var(--text-light); font-size: 20px; }
  .cta-text { left: 0; top: 989px; width: 746px; text-align: center; color: var(--text-light); font-size: 10.3px; line-height: 16px; }
  .cta-btn { left: 330px; top: 1031px; width: 86px; height: 24px; background: var(--brand-grey); color: #fff; font-size: 8px; font-weight: 600; text-align: center; line-height: 24px; }

  /* Footer */
  .site-footer { left: 0; top: 1091px; width: 746px; height: 109px; background: var(--footer-bg); }
  .footer-links { left: 0; top: 1116px; width: 746px; text-align: center; font-size: 10px; color: #f0f0f0; word-spacing: 1px; }
  .footer-links .sep { margin: 0 7px; }
  .copyright { left: 0; top: 1139px; width: 746px; text-align: center; font-size: 8.5px; color: #b8b8b8; }
  .social-foot { left: 327px; top: 1161px; display: flex; gap: 3px; }
  .social-foot span { width: 18px; height: 18px; border-radius: 50%; background: #f0f0f0; display: block; }
</style>
</head>
<body>

<header class="abs site-header">
  <div class="abs brand">Venlox</div>
  <nav class="abs main-nav">
    <span>Home</span><span>Are you a Property Manager</span><span>Contact Us</span>
  </nav>
  <div class="abs social-top"><span></span><span></span><span></span></div>
</header>

<section class="abs hero" role="img" aria-label="Aerial photo of a suburban neighbourhood of houses"></section>
<div class="abs search-panel">
  <h1 class="abs search-title">Find your Local Property Manager</h1>
  <div class="abs field field-type">Select Your Property Type
    <svg width="8" height="5" viewBox="0 0 8 5"><path d="M0 0h8L4 5z" fill="#999"/></svg>
  </div>
  <div class="abs field field-zip">Zipcode</div>
  <div class="abs search-btn">Search</div>
  <p class="abs search-note">Search our directory to find experienced and professional property management companies that meet your needs.</p>
</div>
<div class="abs slider-dots"><span></span><span></span><span></span><span></span></div>

<h2 class="abs steps-heading">To find Property Management Companies near you:</h2>

<div class="abs step" style="left:146px">
  <div class="step-icon">
    <svg width="34" height="28" viewBox="0 0 34 28" fill="none" stroke="#fff" stroke-width="2">
      <rect x="5" y="2" width="24" height="17" rx="1"/>
      <path d="M1 23h32" stroke-width="3"/>
      <path d="M12 11l5-4 5 4M13.5 10v5h7v-5"/>
    </svg>
  </div>
  <p class="step-label">Select your property<br>type and zipcode</p>
</div>
<div class="abs step" style="left:309px">
  <div class="step-icon">
    <svg width="32" height="30" viewBox="0 0 32 30" fill="none" stroke="#fff" stroke-width="2">
      <path d="M2 2h28v19H12l-5 6v-6H2z"/>
      <path d="M8 9h16M8 14h16"/>
    </svg>
  </div>
  <p class="step-label">Review property manager<br>listings in your area</p>
</div>
<div class="abs step" style="left:471px">
  <div class="step-icon">
    <svg width="36" height="30" viewBox="0 0 36 30" fill="#fff">
      <circle cx="18" cy="5" r="3.5"/>
      <rect x="16" y="9" width="4" height="18"/>
      <rect x="4" y="11" width="28" height="2.5"/>
      <path d="M2 17h10a5 4 0 0 1-10 0zM24 17h10a5 4 0 0 1-10 0z"/>
      <rect x="12" y="26" width="12" height="3"/>
    </svg>
  </div>
  <p class="step-label">Select and compare<br>Property Managers</p>
</div>

<section class="abs experience" role="img" aria-label="Photo of a smiling professional woman talking on a phone in a bright office"></section>
<svg class="abs notch" width="16" height="9" viewBox="0 0 16 9"><path d="M0 0h16L8 9z" fill="#fff"/></svg>
<h2 class="abs experience-title">Making renting YOUR home an easy,<br>stress-free experience.</h2>
<ul class="abs benefits">
  <li><svg width="11" height="11" viewBox="0 0 11 11"><circle cx="5.5" cy="5.5" r="5.5" fill="#fbc30a"/><path d="M3 5.7l1.8 1.8L8 4" stroke="#fff" stroke-width="1.4" fill="none"/></svg>Connecting property owners with property managers.</li>
  <li><svg width="11" height="11" viewBox="0 0 11 11"><circle cx="5.5" cy="5.5" r="5.5" fill="#fbc30a"/><path d="M3 5.7l1.8 1.8L8 4" stroke="#fff" stroke-width="1.4" fill="none"/></svg>Providing property management solutions, simplified.</li>
</ul>
<p class="abs experience-copy">Mauris vel lacus vitae felis vestibulum volutpat Etiam est nunc venenatis in tristique eu imperdiet ac nisl Cum sociis natoque penatibus et magnis dis parturient montes nascetur ridiculus mus In iaculis</p>

<section class="abs manager-cta"></section>
<svg class="abs cta-icon" width="44" height="44" viewBox="0 0 44 44" fill="none" stroke="#fff" stroke-width="2">
  <circle cx="22" cy="12" r="8"/>
  <path d="M5 42v-6c0-6 6-10 12-10h10c6 0 12 4 12 10v6z"/>
  <path d="M22 27l-2 4 2 9 2-9z" fill="#fff"/>
</svg>
<h2 class="abs cta-title">Are you a Property Manager?</h2>
<p class="abs cta-text">Join our real estate property management company network. Let us help<br>you find leads of property owners seeking to rent</p>
<div class="abs cta-btn">LEARN MORE</div>

<footer class="abs site-footer"></footer>
<nav class="abs footer-links">Are you a Property Manager<span class="sep">|</span>About Us<span class="sep">|</span>Contact Us<span class="sep">|</span>Term of Use<span class="sep">|</span>Privacy Policy<span class="sep">|</span>Sitemap</nav>
<p class="abs copyright">Copyright © 2014, Venlox, All Rights Reserved</p>
<div class="abs social-foot"><span></span><span></span><span></span><span></span></div>

</body>
</html>
```